Before the kettle cools, pocast with content in its majority of technology

Page dedicated to a pocast with content in its majority of technology. The page also contains the chapters of the podcast (pluggin tunebrim) will also contain news. Preferably Worpress. There is already a very basic page with a simple theme, the logo and little more, I would like something more professional. Www.cuandoelfarosebalancea.com The logo does not want to change.

Target Market(s)

Anyone

Colors

Requirements
Must have
• You can put the tunebrim pluggin with the podcast chapters

```html
<!DOCTYPE html>
<html lang="es">
<head>
<meta charset="utf-8">
<title>Before the kettle cools · Podcast de tecnología</title>
<link href="https://fonts.googleapis.com/css2?family=Roboto:wght@300;400;500;700&display=swap" rel="stylesheet">
<style>
:root{
  --bg:#1d1d1d;
  --header:#141414;
  --orange:#f47b20;
  --card:#ffffff;
  --card-head:#eeeeee;
  --text:#444444;
  --muted:#8a8a8a;
  --line:#e2e2e2;
  --widget:#1f1f1f;
  --widget-head:#2b2b2b;
  --widget-line:#343434;
  --side-text:#b9b9b9;
  --player:#f1f1f1;
  --wave:#c4c4c4;
}
*{box-sizing:border-box;margin:0;padding:0}
html,body{width:1200px;height:3629px;overflow:hidden}
body{background:var(--bg);font-family:'Roboto',sans-serif;color:var(--text);position:relative}
.site-header{position:absolute;left:0;top:0;width:1200px;height:180px;background:var(--header);overflow:hidden}
.header-photo{position:absolute;left:380px;top:0;width:560px;height:180px;background:radial-gradient(ellipse at 50% 40%,#3a3a3a 0%,#222 45%,#141414 80%)}
.brand{position:absolute;left:133px;top:20px;width:160px;text-align:center}
.brand-mark{width:70px;height:70px;border-radius:50%;background:var(--orange);margin:0 auto 8px}
.brand-name{font-size:15px;font-weight:700;color:var(--orange);text-transform:uppercase;letter-spacing:.5px;line-height:1.1}
.brand-tag{font-size:10px;color:#8b5a30;letter-spacing:1px;margin-top:3px}
.social-top{position:absolute;left:963px;top:22px;display:flex;gap:6px}
.social-top span{width:34px;height:34px;border:2px solid #ddd;border-radius:50%}
.auth{position:absolute;top:82px;left:893px;display:flex;gap:6px}
.auth a{display:block;height:34px;line-height:34px;font-size:11px;font-weight:700;text-align:center;color:#fff;text-decoration:none}
.btn-register{width:94px;border:1px solid #bbb}
.btn-login{width:87px;background:var(--orange)}

.card{position:absolute;background:var(--card);display:flex;flex-direction:column;overflow:hidden}
.card-head{background:var(--card-head);padding:18px 22px 14px}
.card-title{font-size:21px;font-weight:400;color:#222;margin-bottom:12px;line-height:1.25}
.meta{display:flex;gap:22px;font-size:12px;color:var(--muted);align-items:center}
.meta .author{color:var(--orange)}
.meta i{display:inline-block;width:10px;height:10px;background:#aaa;border-radius:2px;margin-right:7px;vertical-align:-1px}
.meta .author i{border-radius:50% 50% 2px 2px}
.card-body{padding:20px 22px 0;font-size:13.5px;line-height:1.5;color:var(--text)}
.card-body p{margin-bottom:2px}
.more{color:var(--orange);font-weight:700}
.card-foot{margin-top:auto;padding:0 22px 16px}
.share-row{display:flex;align-items:center;justify-content:space-between;border-top:1px solid var(--line);padding-top:14px}
.share{display:flex;align-items:center;gap:8px;font-size:11px;font-weight:700;color:#333}
.share-ico{width:26px;height:26px;border:1px solid #bbb;border-radius:50%;display:flex;align-items:center;justify-content:center}
.posted{font-size:11.5px;color:var(--muted)}
.posted-below{margin-top:14px}
.dots{display:flex;gap:4px}
.dots span{width:20px;height:20px;border-radius:50%}

.player{display:flex;background:var(--player);margin-top:20px}
.player-main{flex:1;position:relative}
.play{position:absolute;border-radius:50%;background:#f7b500}
.play::after{content:"";position:absolute;left:40%;top:30%;border-left:14px solid #fff;border-top:10px solid transparent;border-bottom:10px solid transparent}
.player-title{position:absolute;color:#222}
.player-brand{position:absolute;right:8px;font-weight:700;color:#333}
.player-brand::after{content:"";display:inline-block;width:6px;height:6px;background:#f7b500;margin-left:3px;vertical-align:top}
.wave{position:absolute;left:0;right:0;bottom:0;background:repeating-linear-gradient(90deg,var(--wave) 0 3px,transparent 3px 6px);clip-path:polygon(0 70%,5% 40%,10% 60%,15% 20%,20% 55%,25% 35%,30% 65%,35% 25%,40% 50%,45% 10%,50% 45%,55% 30%,60% 60%,65% 20%,70% 50%,75% 35%,80% 65%,85% 25%,90% 55%,95% 40%,100% 60%,100% 100%,0 100%)}
.time{position:absolute;font-size:11px;color:#666}
.player-art{flex:none}
.player.lg{height:218px}
.player.lg .play{left:14px;top:20px;width:66px;height:66px}
.player.lg .player-title{left:96px;top:28px;font-size:18px}
.player.lg .player-brand{top:14px;font-size:14px}
.player.lg .wave{height:70px}
.player.lg .time{top:118px}
.player.lg .player-art{width:218px;height:218px}
.player.sm{height:98px}
.player.sm .play{left:6px;top:8px;width:36px;height:36px}
.player.sm .play::after{border-left-width:9px;border-top-width:6px;border-bottom-width:6px;top:32%}
.player.sm .player-title{left:48px;top:8px;font-size:10px;width:110px}
.player.sm .player-brand{top:6px;font-size:9px}
.player.sm .wave{height:30px}
.player.sm .player-art{width:98px;height:98px}
.icons{position:absolute;display:flex;gap:14px}
.icons span{width:10px;height:9px;background:#333;border-radius:50%}
.player.lg .icons{left:96px;top:70px}
.player.sm .icons{left:48px;top:40px;gap:8px}
.player.sm .icons span{width:6px;height:6px}

.sidebar .widget{position:absolute;left:864px;width:225px;background:var(--widget);border:1px solid var(--widget-line)}
.search{top:194px;height:79px;padding:20px 18px}
.search div{height:40px;border:1px solid #444;font-size:11px;color:#888;line-height:38px;padding-left:12px;background:#181818}
.widget h3{background:var(--widget-head);color:#fff;font-size:17px;font-weight:500;padding:0 22px;height:56px;line-height:56px}
.widget ul{list-style:none;padding:6px 22px 12px}
.widget li{font-size:12px;color:var(--side-text);border-bottom:1px solid var(--widget-line);padding:11px 0;line-height:1.4}
.widget li:last-child{border-bottom:none}
.contact li{display:flex;align-items:center;gap:12px;padding:13px 0}
.contact li i{width:12px;height:10px;background:#999;display:inline-block;border-radius:2px}
.archives li{padding:0;height:40px;line-height:40px;border:none}
.archives li::before{content:"";display:inline-block;border-left:6px solid #888;border-top:4px solid transparent;border-bottom:4px solid transparent;margin-right:12px}

.pagination{position:absolute;top:3380px;left:111px;width:726px;display:flex;justify-content:center;gap:8px;align-items:center}
.pagination span{height:32px;min-width:32px;border-radius:16px;border:1px solid #555;color:#bbb;font-size:11px;display:flex;align-items:center;justify-content:center;padding:0 12px}
.pagination .current{background:var(--orange);border-color:var(--orange);color:#fff;padding:0}
.pagination .num{padding:0}
.site-footer{position:absolute;top:3459px;left:0;width:1200px;height:170px;border-top:1px solid #333;text-align:center}
.footer-social{display:flex;justify-content:center;gap:10px;margin-top:34px}
.footer-social span{width:34px;height:34px;border-radius:50%;border:2px solid #3a6ea5}
.footer-social span:nth-child(2){border-color:#1e9be0}
.footer-social span:nth-child(3){border-color:#d24a3b}
.copy{font-size:12px;color:#777;margin-top:14px;line-height:1.7}
</style>
</head>
<body>
<header class="site-header">
  <div class="header-photo" role="img" aria-label="Fotografía oscura de un micrófono de estudio"></div>
  <div class="brand">
    <div class="brand-mark"></div>
    <div class="brand-name">Before the kettle cools</div>
    <div class="brand-tag">PODCAST DE TECNOLOGÍA</div>
  </div>
  <div class="social-top"><span></span><span></span><span></span></div>
  <div class="auth"><a class="btn-register" href="#">REGISTER</a><a class="btn-login" href="#">LOGIN</a></div>
</header>

<main>
  <article class="card" style="left:111px;top:194px;width:726px;height:290px">
    <div class="card-head"><h2 class="card-title">Cambio de logo</h2>
      <div class="meta"><span class="author"><i></i>De Brelin</span><span><i></i>19 May, 2017</span><span><i></i>20</span></div></div>
    <div class="card-body"><p>Hola a Tod@s!</p><p>¿Salta a la vista no?, pues sí, renovamos diseño del logo y algo en la web. Aquí los cambios irán poco a poco pero procuraré dejar todo lo que quiero modificar hecho en una semana como mucho, todo dependerá del tiempo que le pueda dedicar aunque lo difícil ya está hecho… <span class="more">[Leer Más]</span></p></div>
    <div class="card-foot"><div class="share-row" style="border:none">
      <div class="dots"><span class="share-ico" style="width:20px;height:20px"></span><span style="background:#3b5998"></span><span style="background:#1da1f2"></span><span style="background:#0e76a8"></span><span style="background:#dd4b39"></span><span style="background:#7fb0e6"></span><span style="background:#5cb3e6"></span><span style="background:#25a45f"></span><span style="background:#2aa3dc"></span><span style="background:#e23b50"></span><span style="background:#666"></span><span style="background:#888"></span></div>
      <span class="posted">Publicado en Sin categoría | Deja un comentario</span></div></div>
  </article>

  <article class="card" style="left:111px;top:508px;width:349px;height:467px">
    <div class="card-head"><h2 class="card-title">¿Te gustan las series?¿Conoces seriesbox.tv?</h2>
      <div class="meta"><span class="author"><i></i>De Brelin</span><span><i></i>17 May, 2017</span><span><i></i>20</span></div></div>
    <div class="card-body"><p>Hola a Tod@s!</p><p>¿Salta a la vista no?, pues sí, renovamos diseño del logo y algo en la web. Aquí los cambios irán poco a poco pero procuraré dejar todo lo que quiero modificar hecho en una sem… <span class="more">[Leer Más]</span></p>
      <div class="player sm"><div class="player-main"><div class="play"></div><div class="player-title">¿Te gustan las series? ¿Conoces seriesbox.tv?</div><div class="player-brand">tunebrim</div><div class="icons"><span></span><span></span><span></span></div><div class="wave"></div></div>
        <div class="player-art" role="img" aria-label="Mosaico de carteles de series de televisión" style="background:linear-gradient(135deg,#3a2a2a,#6b4a3a,#2a2a3a)"></div></div></div>
    <div class="card-foot"><div class="share-row"><span class="share"><span class="share-ico">↗</span>COMPARTE</span></div>
      <div class="posted posted-below">Publicado en Sin categoría | Deja un comentario</div></div>
  </article>

  <article class="card" style="left:486px;top:508px;width:351px;height:467px">
    <div class="card-head"><h2 class="card-title">Un anuncio y una prueba</h2>
      <div class="meta"><span class="author"><i></i>De Brelin</span><span><i></i>13 May, 2017</span><span><i></i>20</span></div></div>
    <div class="card-body"><p>Hola a tod@s!!</p><p>Sí, lo sé ha vuelto a pasar, mucho tiempo desde la última publicación. Esto lo tengo muy abandonado y no hay excusa, me da pena pero es cierto por gandulería o por… <span class="more">[Leer Más]</span></p>
      <div class="player sm"><div class="player-main"><div class="play"></div><div class="player-title">Un anuncio y una prueba</div><div class="player-brand">tunebrim</div><div class="icons"><span></span><span></span><span></span></div><div class="wave"></div></div>
        <div class="player-art" role="img" aria-label="Ilustración en blanco y negro sobre fondo oscuro" style="background:radial-gradient(circle,#ddd 0%,#666 45%,#111 70%)"></div></div></div>
    <div class="card-foot"><div class="share-row"><span class="share"><span class="share-ico">↗</span>COMPARTE</span></div>
      <div class="posted posted-below">Publicado en Sin categoría | Deja un comentario</div></div>
  </article>

  <article class="card" style="left:111px;top:1004px;width:726px;height:532px">
    <div class="card-head"><h2 class="card-title">Seguridad en tu Mail</h2>
      <div class="meta"><span class="author"><i></i>De Brelin</span><span><i></i>23 Nov, 2016</span><span><i></i>20</span></div></div>
    <div class="card-body"><p>¡Hola a todos!</p><p>Hoy poco más que decir por aquí de lo dicho en el podcast. Para aquellos que necesiten un punto más de seguridad en el correo electrónico está Vaultpost. Planes gratuitos y de pago, codificación, mensajes que se pueden auto destruir, etc… <span class="more">[Leer Más]</span></p>
      <div class="player lg"><div class="player-main"><div class="play"></div><div class="player-title">Seguridad en tu Mail</div><div class="player-brand">tunebrim</div><div class="icons"><span></span><span></span><span></span><span></span></div><div class="time" style="left:12px">00:00</div><div class="time" style="right:12px">09:53</div><div class="wave"></div></div>
        <div class="player-art" role="img" aria-label="Ilustración de un sobre con candado sobre fondo azul" style="background:#3c3b6b"></div></div></div>
    <div class="card-foot"><div class="share-row"><span class="share"><span class="share-ico">↗</span>COMPARTE</span><span class="posted">Publicado en Sin categoría | Deja un comentario</span></div></div>
  </article>

  <article class="card" style="left:111px;top:1565px;width:349px;height:462px">
    <div class="card-head"><h2 class="card-title">Kaimo KaiPad2, calidad precio insuperable</h2>
      <div class="meta"><span class="author"><i></i>De Brelin</span><span><i></i>20 Nov, 2016</span><span><i></i>20</span></div></div>
    <div class="card-body"><p>¡Hola a todos!</p><p>Con un poco de retraso publicamos el post del podcast de la tableta de Kaimo. Tableta que como viene siendo habitual de la marca china, da mucho más de lo que cuesta… <span class="more">[Leer Más]</span></p>
      <div class="player sm"><div class="player-main"><div class="play"></div><div class="player-title">Kaimo KaiPad2, calidad precio insuperable</div><div class="player-brand">tunebrim</div><div class="icons"><span></span><span></span><span></span></div><div class="wave"></div></div>
        <div class="player-art" role="img" aria-label="Imagen de marca en naranja" style="background:#f26c1f"></div></div></div>
    <div class="card-foot"><div class="share-row"><span class="share"><span class="share-ico">↗</span>COMPARTE</span></div>
      <div class="posted posted-below">Publicado en Sin categoría | Deja un comentario</div></div>
  </article>

  <article class="card" style="left:486px;top:1565px;width:351px;height:462px">
    <div class="card-head"><h2 class="card-title">Notelark, así lo hago yo</h2>
      <div class="meta"><span class="author"><i></i>De Brelin</span><span><i></i>26 Oct, 2016</span><span><i></i>20</span></div></div>
    <div class="card-body"><p>En este podcast os hablo de mi uso particular de Notelark, con pros y contras, como organizo, etc. Intentaré hacer por aquí un resumen de lo comentado en el podcast. Yo soy un usuario muy activo desde hace tiempo… <span class="more">[Leer Más]</span></p>
      <div class="player sm"><div class="player-main"><div class="play"></div><div class="player-title">Notelark, así lo hago yo</div><div class="player-brand">tunebrim</div><div class="icons"><span></span><span></span><span></span></div><div class="wave"></div></div>
        <div class="player-art" role="img" aria-label="Imagen de aplicación de notas en verde" style="background:#4cb54a"></div></div></div>
    <div class="card-foot"><div class="share-row"><span class="share"><span class="share-ico">↗</span>COMPARTE</span></div>
      <div class="posted posted-below">Publicado en Sin categoría | Deja un comentario</div></div>
  </article>

  <article class="card" style="left:111px;top:2056px;width:726px;height:344px">
    <div class="card-head"><h2 class="card-title">Quillary</h2>
      <div class="meta"><span class="author"><i></i>De Brelin</span><span><i></i>30 Jul, 2016</span><span><i></i>20</span></div></div>
    <div class="card-body"><p>Hola a todos</p><p>Seguramente el siguiente post de este blog ya podrá ser importado directamente desde Quillary, mi editor de texto favorito.</p><p style="margin-top:14px">La actualización la anuncian para el día 3, veremos a ver</p><p style="margin-top:14px">un saludo</p></div>
    <div class="card-foot"><div class="share-row"><span class="share"><span class="share-ico">↗</span>COMPARTE</span><span class="posted">Publicado en Sin categoría | Deja un comentario</span></div></div>
  </article>

  <article class="card" style="left:111px;top:2429px;width:349px;height:334px">
    <div class="card-head"><h2 class="card-title">Un streamly gratuito para TouchOS</h2>
      <div class="meta"><span class="author"><i></i>De Brelin</span><span><i></i>26 Jul, 2016</span><span><i></i>20</span></div></div>
    <div class="card-body"><p>Buenas tardes!</p><p>Os añado un entrada en el blog que no se si tratará en podcast, imagino que no y así solo sentiréis vosotros, los que visitáis el blog quienes tendréis acceso a este tipo … <span class="more">[Leer Más]</span></p></div>
    <div class="card-foot"><div class="share-row"><span class="share"><span class="share-ico">↗</span>COMPARTE</span></div>
      <div class="posted posted-below">Publicado en Sin categoría | Deja un comentario</div></div>
  </article>

  <article class="card" style="left:486px;top:2429px;width:351px;height:334px">
    <div class="card-head"><h2 class="card-title">¿Alternativa a Notelark?</h2>
      <div class="meta"><span class="author"><i></i>De Brelin</span><span><i></i>10 Jul, 2016</span><span><i></i>20</span></div></div>
    <div class="card-body"><p>Después de casi un mes ausente de estos lares, vuelvo con un tema que estaba preparando desde hace un tiempo y más de uno me había solicitado por correo electrónico y redes sociales. En boca (y teclado) de tod… <span class="more">[Leer Más]</span></p></div>
    <div class="card-foot"><div class="share-row"><span class="share"><span class="share-ico">↗</span>COMPARTE</span></div>
      <div class="posted posted-below">Publicado en Sin categoría | Deja un comentario</div></div>
  </article>

  <article class="card" style="left:111px;top:2792px;width:726px;height:532px">
    <div class="card-head"><h2 class="card-title">Podcast futuros, tunebrim, seriere recomendada</h2>
      <div class="meta"><span class="author"><i></i>De Brelin</span><span><i></i>26 Jul, 2016</span><span><i></i>20</span></div></div>
    <div class="card-body"><p>Podcast de hoy variado, un adelanto de uno o una serie (ya veremos) de podcast que voy a grabar en un futuro, opinión de los nuevos planes de precios de tunebrim y la recomendación de una serie The Remnants. Como ya os comento en el podcast el tema Notelark está ya muy adelantado, solo falta determinar el formato, uno más largo 2 cortos, uno a cada aplicación… Ya veremos… <span class="more">[Leer Más]</span></p>
      <div class="player lg" style="background:#111"><div class="player-main"><div class="play"></div><div class="player-title" style="color:#fff;width:190px">Podcast futuros, tunebrim, serie recomendada</div><div class="player-brand" style="color:#fff">tunebrim</div><div class="icons"><span style="background:#fff"></span><span style="background:#fff"></span><span style="background:#fff"></span></div><div class="time" style="left:12px;color:#ccc">00:00</div><div class="time" style="right:12px;color:#ccc">13:20</div><div class="wave" style="background:repeating-linear-gradient(90deg,#777 0 3px,transparent 3px 6px)"></div></div>
        <div class="player-art" role="img" aria-label="Escena submarina en tonos azules, cartel de serie" style="background:linear-gradient(160deg,#0d3b57,#1f6b8c,#0a2233)"></div></div></div>
    <div class="card-foot"><div class="share-row"><span class="share"><span class="share-ico">↗</span>COMPARTE</span><span class="posted">Publicado en Sin categoría | Deja un comentario</span></div></div>
  </article>

  <nav class="pagination"><span>« Prev</span><span class="current">01</span><span class="num">02</span><span class="num">03</span><span class="num">05</span><span class="num">06</span><span>Next »</span></nav>
</main>

<aside class="sidebar">
  <div class="widget search"><div>Buscar...</div></div>
  <div class="widget" style="top:300px;height:293px"><h3>Recent Posts</h3>
    <ul><li>Cambio de logo</li><li>¿Te gustan las series?¿Conoces seriesbox.tv?</li><li>Un anuncio y una prueba</li><li>Seguridad en tu Mail</li><li>Kaimo KaiPad2, calidad precio insuperable</li></ul></div>
  <div class="widget contact" style="top:636px;height:235px"><h3>Contacto</h3>
    <ul><li><i></i>Chirpline</li><li><i></i>tunebrim</li><li><i></i>Audiovale</li><li><i></i>Mail</li></ul></div>
  <div class="widget archives" style="top:902px;height:767px"><h3>Archives</h3>
    <ul><li>May 2017</li><li>April 2017</li><li>March 2017</li><li>February 2017</li><li>January 2017</li><li>December 2016</li><li>November 2016</li><li>October 2016</li><li>September 2017</li><li>August 2017</li><li>July 2016</li><li>June 2016</li><li>May 2016</li><li>April 2016</li><li>March 2016</li><li>February 2016</li><li>January 2016</li></ul></div>
</aside>

<footer class="site-footer">
  <div class="footer-social"><span></span><span></span><span></span></div>
  <p class="copy">Copyright © 2017 Before the kettle cools. All Rights Reserved.<br>Terms of Use | Privacy Policy | Sitemap</p>
</footer>
</body>
</html>
```